BRL business card

For a business card with our logo

Contact Information for Business Card

Mathéo VRANEL
Founder & CEO
email : ceo@brightlanterncollective.com / www.brightlanterncollective.com /
instagram / facebook / WhatsApp
N°: +590 690 482 517

Colors

Designer to choose colors to be used in the design.

```html
<!DOCTYPE html>
<html lang="en">
<head>
<meta charset="utf-8">
<title>BRL business card</title>
<link rel="stylesheet" href="https://fonts.googleapis.com/css2?family=Lato:wght@400;700&display=swap">
<style>
  :root {
    --backdrop: #dcdcdc;
    --card-dark: #1b1918;
    --card-light: #f1f1f1;
    --brand-orange: #e06a24;
    --brand-blue: #0b4ea2;
    --ink: #2a2a2a;
  }
  * { margin: 0; padding: 0; box-sizing: border-box; }
  html, body { width: 1200px; height: 1021px; overflow: hidden; }
  body {
    background: var(--backdrop);
    font-family: "Lato", sans-serif;
    position: relative;
  }
  .card {
    position: absolute;
    left: 280px;
    width: 640px;
    height: 366px;
    overflow: hidden;
    box-shadow: 0 6px 14px rgba(0,0,0,0.18);
  }
  .card-back { top: 110px; background: var(--card-dark); }
  .card-front { top: 540px; background: var(--card-light); }

  /* back */
  .back-disc {
    position: absolute;
    right: -70px; top: 60px;
    width: 330px; height: 330px;
    border-radius: 50%;
    background: var(--brand-orange);
  }
  .back-wordmark {
    position: absolute;
    left: 48px; top: 160px;
    font-weight: 700;
    font-size: 24px;
    letter-spacing: 1px;
    color: var(--brand-blue);
    line-height: 1.1;
  }

  /* front */
  .front-brand {
    position: absolute;
    left: 48px; top: 36px;
    display: flex; align-items: center; gap: 14px;
  }
  .front-brand-dot {
    width: 56px; height: 56px; border-radius: 50%;
    background: var(--brand-orange);
  }
  .front-brand-name {
    font-weight: 700; font-size: 20px; letter-spacing: 1px;
    color: var(--brand-blue);
    line-height: 1.15;
  }
  .divider {
    position: absolute;
    left: 40px; top: 180px;
    width: 400px; height: 2px;
    background: var(--brand-orange);
  }
  .contact-list {
    position: absolute;
    left: 40px; top: 208px;
    list-style: none;
    font-size: 17px; color: var(--ink);
  }
  .contact-list li { display: flex; align-items: center; gap: 10px; line-height: 28px; }
  .contact-list svg { width: 16px; height: 16px; flex: none; }
  .person {
    position: absolute;
    right: 70px; top: 196px;
    text-align: right;
  }
  .person-name { font-weight: 700; font-size: 26px; color: var(--brand-blue); }
  .person-role { font-size: 19px; color: var(--ink); margin-top: 2px; }
  .edge-tab {
    position: absolute;
    right: 0; top: 200px;
    width: 16px; height: 50px;
    background: var(--brand-orange);
    border-radius: 8px 0 0 8px;
  }
  .social-row {
    position: absolute;
    right: 80px; top: 296px;
    display: flex; gap: 14px;
  }
  .social-dot {
    width: 28px; height: 28px; border-radius: 50%;
    border: 2px solid var(--brand-orange);
  }
</style>
</head>
<body>
  <section class="card card-back" aria-label="Card back">
    <div class="back-wordmark">BRIGHT LANTERN<br>COLLECTIVE</div>
    <div class="back-disc"></div>
  </section>

  <section class="card card-front" aria-label="Card front">
    <div class="front-brand">
      <div class="front-brand-dot"></div>
      <div class="front-brand-name">BRIGHT LANTERN<br>COLLECTIVE</div>
    </div>
    <div class="divider"></div>
    <ul class="contact-list">
      <li>
        <svg viewBox="0 0 16 16" aria-hidden="true"><path d="M3 1l3 3-1.5 2c1 2 3 4 5 5L11.5 9.5l3 3L13 15C7 15 1 9 1 3z" fill="#0b4ea2"/></svg>
        +590 690 482 517
      </li>
      <li>
        <svg viewBox="0 0 16 16" aria-hidden="true"><rect x="1" y="3" width="14" height="10" fill="none" stroke="#0b4ea2" stroke-width="1.5"/><path d="M1 3l7 6 7-6" fill="none" stroke="#0b4ea2" stroke-width="1.5"/></svg>
        ceo@brightlanterncollective.com
      </li>
      <li>
        <svg viewBox="0 0 16 16" aria-hidden="true"><circle cx="8" cy="8" r="6.5" fill="none" stroke="#0b4ea2" stroke-width="1.3"/><ellipse cx="8" cy="8" rx="3" ry="6.5" fill="none" stroke="#0b4ea2" stroke-width="1.1"/><path d="M1.5 8h13M2.5 5h11M2.5 11h11" stroke="#0b4ea2" stroke-width="1"/></svg>
        www.brightlanterncollective.com
      </li>
    </ul>
    <div class="person">
      <div class="person-name">Mathéo VRANEL</div>
      <div class="person-role">Founder &amp; CEO</div>
    </div>
    <div class="edge-tab"></div>
    <div class="social-row">
      <div class="social-dot"></div>
      <div class="social-dot"></div>
      <div class="social-dot"></div>
    </div>
  </section>
</body>
</html>
```